Canadian Christian Church needs design for new sermon series

A graphic design for our series and an invitation card to invite people to the series. Check design brief for more detailed information. Target audience: young families and young adults. Looking for a creative design that will get people's attention and create interest. See design brief for copy of design purchased for previous series.
Updates
entered Apr 4 incorrectly. Need a week to receive and review designs, and today is Apr 2/19. Thanks!
Target Market(s)
young families and young adults
Colors
Designer to choose colors to be used in the design.
Look and feel

```html
<!DOCTYPE html>
<html lang="en">
<head>
<meta charset="utf-8">
<title>Messy – Sermon Series Invitation</title>
<link href="https://fonts.googleapis.com/css2?family=Montserrat:wght@500;600;700;800&family=Cinzel:wght@700&family=Cormorant+Garamond:wght@600&family=Lato:wght@400&display=swap" rel="stylesheet">
<style>
  :root {
    --page: #e2e2e2;
    --paper: #d9d1c3;
    --ink: #3b302c;
    --band: #40332f;
    --back: #c4baa5;
    --back-light: #d6cebf;
    --white: #ffffff;
    --rule: #f3efe8;
  }
  * { margin: 0; padding: 0; box-sizing: border-box; }
  html, body { width: 1200px; height: 1200px; overflow: hidden; background: var(--page); }
  body { position: relative; font-family: "Montserrat", sans-serif; }

  .card { position: absolute; left: 296px; width: 609px; overflow: hidden; }

  /* Front */
  .card-front { top: 120px; height: 479px; background: linear-gradient(100deg, var(--paper) 0%, #cfc6b6 60%, #bdb3a2 100%); }
  .photo { position: absolute; left: 296px; top: 0; width: 313px; height: 479px;
    background: radial-gradient(ellipse at 60% 45%, #8a7f75 0%, #5b514a 35%, #2f2824 75%),
                linear-gradient(180deg, #3a322d, #9c928a);
    background-blend-mode: multiply; }
  .photo::after { content: ""; position: absolute; left: 0; right: 0; bottom: 0; height: 180px;
    background: linear-gradient(180deg, rgba(200,190,176,0), rgba(205,196,182,.85)); }
  .frame { position: absolute; left: 9px; top: 13px; width: 583px; height: 456px; border: 1.5px solid var(--ink); }
  .church-mark { position: absolute; left: 322px; top: 172px; width: 180px; text-align: center; color: var(--ink); }
  .church-mark .dot { width: 48px; height: 48px; border-radius: 50%; background: var(--ink); margin: 0 auto 14px; }
  .church-mark .name { font: 600 14px "Montserrat", sans-serif; white-space: nowrap; }
  .series-title { position: absolute; left: 318px; top: 341px; font: 800 72px/1 "Montserrat", sans-serif; color: var(--ink); letter-spacing: 1px; }
  .series-banner { position: absolute; left: 323px; top: 416px; width: 501px; height: 50px; background: var(--band);
    color: var(--white); font: 700 33px/50px "Cinzel", serif; text-align: center; letter-spacing: 0; }
  .front-url { position: absolute; left: 323px; top: 560px; font: 600 16px "Cormorant Garamond", serif; color: var(--white); letter-spacing: 2.5px; }

  /* Back */
  .card-back { top: 662px; height: 480px; background: linear-gradient(160deg, var(--back-light) 0%, var(--back) 55%, #bdb29c 100%); }
  .swooshes { position: absolute; inset: 0; }
  .invite { position: absolute; left: 0; width: 609px; text-align: center; color: var(--white); }
  .invite-title { top: 24px; font: 800 44px/1 "Montserrat", sans-serif; }
  .invite-time { top: 72px; font: 700 34px/1 "Montserrat", sans-serif; }
  .topics-tab { position: absolute; left: 24px; top: 145px; width: 168px; height: 28px; background: var(--band);
    color: var(--white); font: 700 15px/28px "Montserrat", sans-serif; padding-left: 6px; letter-spacing: .3px; }
  .topics { position: absolute; left: 24px; top: 173px; width: 364px; border-collapse: collapse; border: 1.5px solid var(--band); }
  .topics td { height: 26px; border: 1.5px solid var(--band); color: var(--white); font: 700 16px/1 "Montserrat", sans-serif; padding: 2px 0 0 10px; letter-spacing: .3px; }
  .topics td.date { width: 122px; }
  .side { position: absolute; left: 415px; width: 180px; color: var(--ink); }
  .side h2 { font: 700 16px/1.25 "Montserrat", sans-serif; letter-spacing: .5px; padding-bottom: 6px; border-bottom: 1px solid var(--rule); width: 144px; }
  .features { top: 142px; }
  .features ul { list-style: none; margin-top: 12px; font: 400 9px/1.25 "Lato", sans-serif; }
  .features li { position: relative; padding-left: 8px; margin-bottom: 5px; }
  .features li::before { content: "•"; position: absolute; left: 0; }
  .about { top: 303px; }
  .about p { margin-top: 12px; font: 400 7.3px/1.3 "Lato", sans-serif; width: 170px; }
  .contact-band { position: absolute; left: 0; bottom: 0; width: 609px; height: 60px; background: var(--band);
    color: var(--white); text-align: center; font: 500 12.5px/1.5 "Montserrat", sans-serif; padding-top: 11px; }
</style>
</head>
<body>

<section class="card card-front">
  <div class="photo" role="img" aria-label="Sepia photo of a child peeking through torn paper, fingers gripping the edge"></div>
  <div class="frame"></div>
  <div class="church-mark" style="left:26px;top:52px;">
    <div class="dot"></div>
    <div class="name">Maple Grove Family Church</div>
  </div>
  <h1 class="series-title" style="left:22px;top:221px;">MESSY</h1>
  <div class="series-banner" style="left:27px;top:296px;">JOINING GOD IN THE MESS</div>
  <div class="front-url" style="left:27px;top:440px;">www.maplegrovechurch.ca</div>
</section>

<section class="card card-back">
  <svg class="swooshes" viewBox="0 0 609 480" aria-hidden="true">
    <path d="M10 0 C 120 110, 300 150, 609 120" fill="none" stroke="#e4ddd1" stroke-width="1.5" opacity=".7"/>
    <path d="M0 40 C 60 140, 40 260, 30 480" fill="none" stroke="#ddd5c7" stroke-width="1.5" opacity=".6"/>
    <path d="M0 150 C 200 110, 420 100, 609 180 L609 0 L0 0 Z" fill="#ffffff" opacity=".08"/>
    <path d="M380 0 C 520 60, 590 200, 609 260" fill="none" stroke="#ddd5c7" stroke-width="1.2" opacity=".6"/>
  </svg>
  <div class="invite invite-title">JOIN US</div>
  <div class="invite invite-time">Sundays @ 10:30</div>

  <div class="topics-tab">MESSAGE TOPICS</div>
  <table class="topics">
    <tr><td class="date">April 28th</td><td>We Made This Mess</td></tr>
    <tr><td class="date">May 5th</td><td>Bless in the Mess</td></tr>
    <tr><td class="date">May 12th</td><td>Born into the Mess</td></tr>
    <tr><td class="date">May 19th</td><td>Messy Work</td></tr>
    <tr><td class="date">May 26th</td><td>Messy Church</td></tr>
    <tr><td class="date">June 2nd</td><td>Messy Hospitality</td></tr>
    <tr><td class="date">June 9th</td><td>TBD</td></tr>
    <tr><td class="date">June 16th</td><td>Messy within Boundaries</td></tr>
  </table>

  <div class="side features">
    <h2>FEATURES OF<br>THE SERVICE:</h2>
    <ul>
      <li>Staffed nursery &amp; children's program every Sunday</li>
      <li>Coffee &amp; snacks</li>
      <li>Everyone welcome</li>
    </ul>
  </div>
  <div class="side about">
    <h2>ABOUT THE<br>CHURCH</h2>
    <p>Maple Grove Family Church is a multicultural, multi-generational Christian community, serving Brookfield and Lakeview. We are a part of the Northern Fellowship of Churches.</p>
  </div>

  <footer class="contact-band">
    Location - 1185 Harbour Road West Brookfield, ON&nbsp; L4N 2P7<br>
    Phone-905.555.0142 | Email-info@maplegrovechurch.ca | Website-www.maplegrovechurch.ca
  </footer>
</section>

</body>
</html>
```